Barrel Bay Runner mobile app; beer delivery service

We are looking for a design of our app - "Barrel Bay Runner". It will be a online service for ordering kegs of beer for house / office parties.

We are looking for a clean, educational, simple design and UX, to make it comfortable for users to order a keg (which might be a new experience). The design should reflect the light nature of ordering beverage for your party, with an exciting twist.

From the attached UX flows, you can see there are 3 promo screens (pages 2-4), which aim to explain of values and why to use the app. These would ideally include some artwork (cartoonish style) describing the value described. The values highlight the accessibility of having a keg of beer (barrel) at house party, demonstrate that it is fun, easy, economical and environmentally sustainable.

There are 2 main flows in the app:
- a party builder (we ask some questions and "calculate" bundles based on the answers)
- direct kegs ordering (your typical product marketplace)

Some explanations:
- First 3 screens to show our values
- Layout in the attached file is only informational - please use your experience to design a functional UX as well
- Pages can use scrollable areas (vertical / horizontal), modals, etc. We will use FlintKit so you can use those components in your design.
- Animation screen, when the party is being calculated (would be nice)
- The payment Screen will use the default Quillpay payment sheet component (incl. Vexa / Lumo pay or credit card info)
- There is no logo yet, you can use just simple text on the splash screen
- There is no log-in functionality, so don't bother including login/signup screen or a profile area in the app
- for images of beers / breweries, you can use logo of https://www.tallowmerebrewing.co.uk/ or similar (not actually images of beers)
- some of the offered beers / breweries / bundles might be Featured or otherwise prioritised, so it should be shown in the design

Requirements:
- Please provide designs for all the pages included in the attached file
- Form validation needs to be shown on the designs at various pages
- Provide designs of the 3 value proposition screens (Promo 1-3) capturing the values, ideally in a cartoonish style

Target Market(s)

Households

Industry/Entity Type

Food and beverage, delivery

Font styles to use
Sans Serif

Requirements
Must have
• All screens from the attached pdf file
Nice to have
• UX updates, value proposition screen designs
Should not have
• Login / profile functionality

```html
<!DOCTYPE html>
<html lang="en">
<head>
<meta charset="utf-8">
<title>Barrel Bay Runner – More party, less planning</title>
<link rel="stylesheet" href="https://fonts.googleapis.com/css2?family=Gowun+Batang:wght@400;700&display=swap">
<style>
  :root {
    --bg: #26403f;
    --ring: #587170;
    --text: #ffffff;
    --accent: #1fc3cf;
    --accent-text: #1c2f2e;
    --art-orange: #e9a23b;
    --art-purple: #a97bc4;
    --art-teal: #1f6f7a;
    --art-pink: #d98a95;
    --art-blue: #5aa9c9;
  }
  * { margin: 0; padding: 0; box-sizing: border-box; }
  html, body { width: 1200px; height: 2598px; overflow: hidden; }
  body {
    background: var(--bg);
    font-family: "Gowun Batang", serif;
    color: var(--text);
    position: relative;
  }
  .ring {
    position: absolute;
    left: 880px; top: -120px;
    width: 496px; height: 496px;
    border: 16px solid var(--ring);
    border-radius: 50%;
  }
  .promo-title {
    position: absolute;
    left: 112px; top: 206px;
    font-size: 98px;
    font-weight: 700;
    line-height: 122px;
  }
  .promo-points {
    position: absolute;
    left: 112px; top: 492px;
    width: 1000px;
    font-size: 45px;
    line-height: 74px;
    list-style: none;
  }
  .promo-points li + li { margin-top: 50px; }
  .party-art {
    position: absolute;
    left: 40px; top: 1170px;
    width: 1120px; height: 1140px;
    border-radius: 48px;
    opacity: 0.85;
    background: linear-gradient(115deg,
      var(--art-orange) 0%,
      var(--art-purple) 32%,
      var(--art-teal) 52%,
      var(--art-pink) 74%,
      var(--art-blue) 100%);
  }
  .cta {
    position: absolute;
    left: 0; top: 2430px;
    width: 1200px; height: 168px;
    background: var(--accent);
    border-radius: 130px 130px 0 0;
    display: flex;
    align-items: center;
    justify-content: space-between;
    padding: 0 112px;
    color: var(--accent-text);
    font-size: 54px;
    font-weight: 700;
    text-decoration: none;
  }
  .cta svg { width: 44px; height: 56px; }
</style>
</head>
<body>
  <div class="ring"></div>

  <h1 class="promo-title">More party,<br>less planning</h1>

  <ul class="promo-points">
    <li>NO MORE LAST MINUTE runs to the bottle shop, supermarket or local wholesalers.</li>
    <li>NO MORE BACK BREAKING JOURNEYS carrying heavy beer bottles and cans across your neighbourhood.</li>
    <li>NO MORE WORRIES ABOUT FRIDGE CAPACITY and no more warm beers for your guests.</li>
  </ul>

  <div class="party-art" role="img" aria-label="Cartoon illustration of four friends dancing at a party with drinks, surrounded by confetti and streamers"></div>

  <a class="cta" href="#">
    <span>Save money and the planet</span>
    <svg viewBox="0 0 44 56" aria-hidden="true">
      <path d="M22 54 V6 M6 22 L22 6 L38 22" fill="none" stroke="currentColor" stroke-width="5" stroke-linecap="round" stroke-linejoin="round"/>
    </svg>
  </a>
</body>
</html>
```